Tova Brisk Fitness Coaching Project

I am a personal trainer based in London. My services include one-on-one PT sessions, bootcamps.
I would like the design to be minimalistic. With light colours: white, pink, purple.
I specialise in weight loss, flexibility, mobility.

Tova Penrick
Personal Trainer
Email: tova.penrick@mailgrove.net
tel: 07500 918 243
Instagram: Tova Brisk

Target Market(s)

adults, mostly females (age 18-50).

Industry/Entity Type

Fitness

Contact Information for Business Card

Tova Penrick
Personal Trainer
tel: 07500 918 243
Instagram: Tova Brisk

Font styles to use
Serif

Colors
eea4c8
fbd4d5
fdf9cf
cfeae6
cee9f5

Requirements
Nice to have
• minimalistic style
• easy to read and remember

```html
<!DOCTYPE html>
<html lang="en">
<head>
<meta charset="utf-8">
<title>Tova Penrick – Personal Trainer Business Card</title>
<link rel="stylesheet" href="https://fonts.googleapis.com/css2?family=Josefin+Sans:wght@300;400;600&display=swap">
<style>
  :root {
    --backdrop: #ececec;
    --card-white: #ffffff;
    --card-cream: #fcf7cf;
    --ray-blush: #f9e3cf;
    --brand-pink: #eea4c8;
    --text-grey: #555555;
    --shadow: rgba(0, 0, 0, 0.12);
  }
  * { margin: 0; padding: 0; box-sizing: border-box; }
  html, body {
    width: 1200px;
    height: 800px;
    overflow: hidden;
    background: var(--backdrop);
    font-family: "Josefin Sans", sans-serif;
  }
  .canvas {
    position: relative;
    width: 1200px;
    height: 800px;
    display: flex;
    align-items: center;
    justify-content: center;
    gap: 60px;
  }
  .card {
    position: relative;
    width: 500px;
    height: 286px;
    box-shadow: 0 10px 30px var(--shadow);
    overflow: hidden;
  }

  /* Back side: white with contact details */
  .card--back { background: var(--card-white); }
  .card--back .brand {
    position: absolute;
    left: 40px;
    bottom: 46px;
  }
  .contact-list {
    position: absolute;
    right: 40px;
    top: 60px;
    list-style: none;
    display: flex;
    flex-direction: column;
    gap: 16px;
  }
  .contact-item {
    display: flex;
    align-items: center;
    gap: 12px;
    font-size: 15px;
    font-weight: 400;
    color: var(--text-grey);
  }
  .contact-icon {
    width: 22px;
    height: 22px;
    flex: none;
  }

  /* Front side: cream with sunburst decoration */
  .card--front { background: var(--card-cream); }
  .sunburst {
    position: absolute;
    inset: 0;
    background:
      radial-gradient(circle at 50% 50%, var(--ray-blush) 0%, rgba(249, 227, 207, 0.55) 35%, rgba(252, 247, 207, 0) 75%);
  }
  .card--front .brand {
    position: absolute;
    left: 50%;
    top: 50%;
    transform: translate(-50%, -50%);
    text-align: left;
  }

  /* Brand wordmark */
  .brand-name {
    display: flex;
    align-items: center;
    gap: 10px;
    font-size: 30px;
    font-weight: 600;
    letter-spacing: 1px;
    text-transform: uppercase;
    color: var(--brand-pink);
    line-height: 1;
  }
  .brand-dot {
    width: 14px;
    height: 14px;
    border-radius: 50%;
    background: var(--brand-pink);
    flex: none;
  }
  .brand-role {
    margin-top: 6px;
    margin-left: 24px;
    font-size: 12px;
    font-weight: 400;
    letter-spacing: 1.5px;
    text-transform: uppercase;
    color: var(--text-grey);
  }
</style>
</head>
<body>
<main class="canvas">

  <section class="card card--back" aria-label="Business card, contact side">
    <div class="brand">
      <div class="brand-name"><span class="brand-dot"></span>Tova Penrick</div>
      <div class="brand-role">Personal Trainer</div>
    </div>

    <ul class="contact-list">
      <li class="contact-item">
        <svg class="contact-icon" viewBox="0 0 22 22" aria-hidden="true">
          <circle cx="11" cy="11" r="11" fill="var(--brand-pink)"/>
          <path d="M8 6.5c.6 0 1.2 1.6 1.2 2.1 0 .6-.8.8-.7 1.3.3 1 1.3 2 2.3 2.3.5.1.7-.7 1.3-.7.5 0 2.1.6 2.1 1.2 0 .9-1 1.8-2 1.6-2.8-.5-5.1-2.8-5.6-5.6C6.4 7.6 7.2 6.5 8 6.5z" fill="#fff"/>
        </svg>
        <span>07500 918 243</span>
      </li>
      <li class="contact-item">
        <svg class="contact-icon" viewBox="0 0 22 22" aria-hidden="true">
          <circle cx="11" cy="11" r="11" fill="var(--brand-pink)"/>
          <rect x="6" y="7.5" width="10" height="7" rx="1" fill="none" stroke="#fff" stroke-width="1.3"/>
          <path d="M6.3 8l4.7 3.6L15.7 8" fill="none" stroke="#fff" stroke-width="1.3"/>
        </svg>
        <span>tova.penrick@mailgrove.net</span>
      </li>
      <li class="contact-item">
        <svg class="contact-icon" viewBox="0 0 22 22" aria-hidden="true">
          <circle cx="11" cy="11" r="11" fill="var(--brand-pink)"/>
        </svg>
        <span>Tova Brisk</span>
      </li>
    </ul>
  </section>

  <section class="card card--front" aria-label="Business card, brand side">
    <div class="sunburst" role="img" aria-label="Soft pink sunburst rays radiating from the centre over a pale cream background"></div>
    <div class="brand">
      <div class="brand-name"><span class="brand-dot"></span>Tova Penrick</div>
      <div class="brand-role">Personal Trainer</div>
    </div>
  </section>

</main>
</body>
</html>
```